"Tarvel Mouthguards " Custom-made Mouthguard Business Website

We need an informational website for our mouthguard Business "Tarvel Mouthguards". The logo is navy blue/lime green so want to have colour scheme that goes nicely with this - have uploaded our mouthguard flyer with some information we need to put into the website but I do have more information to put in there.

Target Market(s)

Sports clubs, sportspeople, parents and kids, schools

Industry/Entity Type

Dental, Custom-made Sports Mouthguards

Coding

Number of Pages Required

5+ page

Font styles to use
Serif
Sans Serif

Colors
0054AA
0677BA
7BADD7
CADEEF
E8F1F8
0094D4
00A9DD
6FCCEA
C7EBF8
E9F6FB
00AB8E
00BBA5
67D7C9
C6EFE9
E9F9F6
59FF00
82FF00
B8FF75
E3FFCB
F4FFEA
FFF300
FFF600
FEFA6F
FFFEC7
FFFEE8
FFC000
F8CF3A
FAE287
FDF2CF
FEFAEE
F0912C
F2A743
F7CA91
FBE8D2
FDF5EE
EE7325
F08F49
F5BC92
FAE3D3
FDF4ED

Requirements
Must have
• I want drop down pages, not one scrolling page. Different pages for each heading . Content uploaded - We need a general home page with lots of pictures and info that I'll provide. A page each dedicated to 1) About Us 2) Why choose a custom mouthguard? 3) Gallery 4) Contact Us. Will need logos from "Morvex"
Nice to have
• Mainly use greens and blues, but happy to pop in some yellow/oranges/red oranges if it looks good

```html
<!DOCTYPE html>
<html lang="en">
<head>
<meta charset="utf-8">
<title>Tarvel Mouthguards</title>
<link href="https://fonts.googleapis.com/css2?family=Michroma&family=Lato:wght@400;700&display=swap" rel="stylesheet">
<style>
:root{
  --navy:#0b2566;
  --green:#3dcc2e;
  --grass:#6da14c;
  --ink:#1c1c1c;
  --white:#ffffff;
  --head:"Michroma",sans-serif;
  --body:"Lato",sans-serif;
}
*{box-sizing:border-box;margin:0;padding:0}
html,body{width:1200px;height:3379px;overflow:hidden;background:var(--white);color:var(--ink);font-family:var(--body)}
.page{position:relative;width:1200px;height:3379px}
.abs{position:absolute}
.brand{font-family:var(--head);font-weight:400;color:var(--navy);line-height:1.05;letter-spacing:1px}
.topbar .contact{display:flex;align-items:center;gap:12px;font-family:var(--head);font-size:14px;color:var(--navy);white-space:nowrap}
.icon-circle{width:42px;height:42px;border-radius:50%;border:3px solid var(--navy);display:flex;align-items:center;justify-content:center}
.icon-circle span{width:28px;height:28px;border-radius:50%;background:var(--green);display:flex;align-items:center;justify-content:center}
.mainnav{top:86px;left:0;width:1200px;height:42px;background:var(--navy)}
.mainnav a{position:absolute;top:0;height:42px;display:flex;align-items:center;font-family:var(--head);font-size:12px;color:var(--white);text-decoration:none;text-transform:uppercase;white-space:nowrap}
.mainnav a.current{color:var(--green)}
.mainnav .cta{right:0;left:auto;width:237px;background:var(--green);justify-content:center;font-size:14px}
.btn{display:inline-flex;align-items:center;gap:12px;height:44px;padding:0 22px;border-radius:22px;font-family:var(--head);font-size:15px;color:var(--white);white-space:nowrap}
.btn i{width:22px;height:22px;border-radius:50%;background:var(--white);display:flex;align-items:center;justify-content:center}
.btn i::after{content:"";width:10px;height:10px;border-radius:50%;background:var(--green);border:2px solid var(--navy)}
.btn.navy{background:var(--navy)}
.btn.green{background:var(--green)}
.section-title{font-family:var(--head);font-size:30px;color:var(--ink);text-align:center;text-transform:uppercase}
.rule{height:3px;width:74px;background:var(--green)}
.feature{position:absolute;width:180px;text-align:center;font-family:var(--head);font-size:13px;line-height:1.65;color:var(--ink)}
.feature .ring{width:88px;height:88px;margin:0 auto 24px;border-radius:50%;border:5px solid var(--navy);display:flex;align-items:center;justify-content:center}
.feature .ring span{width:64px;height:64px;border-radius:50%;border:3px solid var(--green);display:flex;align-items:center;justify-content:center}
.points li{list-style:none;display:flex;gap:12px;margin-bottom:22px;font-size:15px;line-height:1.55;color:var(--white)}
.points li::before{content:"";flex:0 0 14px;height:14px;margin-top:5px;border-radius:50%;border:3px solid var(--white);background:var(--green)}
.points b{font-size:17px;font-weight:700}
.tile{position:absolute;border-radius:10px}
.footnav{display:flex;justify-content:center;gap:47px;font-size:15px;text-transform:uppercase;color:var(--ink)}
.fcontact{position:absolute;display:flex;gap:14px;font-family:var(--head);font-size:14px;color:var(--navy);line-height:1.7;white-space:nowrap}
.fcontact .ring{flex:0 0 44px;height:44px;border-radius:50%;border:3px solid var(--navy);display:flex;align-items:center;justify-content:center}
.fcontact .ring span{width:28px;height:28px;border-radius:50%;background:var(--green);display:flex;align-items:center;justify-content:center}
.divider{position:absolute;width:2px;height:42px;background:var(--green)}
</style>
</head>
<body>
<div class="page">

<div class="abs brand" style="top:12px;left:113px;font-size:24px">TARVEL<br><span style="font-size:17px">MOUTHGUARDS</span></div>
<div class="abs topbar" style="top:18px;left:390px;display:flex;gap:24px">
  <div class="contact"><div class="icon-circle"><span><svg width="14" height="14" viewBox="0 0 24 24"><path fill="#fff" d="M6.6 10.8a15 15 0 0 0 6.6 6.6l2.2-2.2c.3-.3.7-.4 1-.2 1.1.4 2.3.6 3.6.6.6 0 1 .4 1 1V20c0 .6-.4 1-1 1A17 17 0 0 1 3 4c0-.6.4-1 1-1h3.5c.6 0 1 .4 1 1 0 1.3.2 2.5.6 3.6.1.3 0 .7-.2 1z"/></svg></span></div>PHONE: 08 6100 2755</div>
  <div class="contact"><div class="icon-circle"><span><svg width="14" height="14" viewBox="0 0 24 24"><path fill="#fff" d="M3 5h18v14H3zm2 2v.5l7 4.5 7-4.5V7z"/></svg></span></div>EMAIL: info@westshoredenture.com.au</div>
</div>

<nav class="abs mainnav">
  <a class="current" href="#" style="left:113px">Home</a>
  <a href="#" style="left:216px">About Us</a>
  <a href="#" style="left:359px">Why Choose a Custom Mouthguard?</a>
  <a href="#" style="left:765px">Gallery</a>
  <a href="#" style="left:890px">FAQ</a>
  <a class="cta" href="#">Contact Us</a>
</nav>

<svg class="abs" style="top:128px;left:0" width="1200" height="560" viewBox="0 0 1200 560">
  <defs>
    <linearGradient id="heroFill" x1="0" y1="0" x2="1" y2="0">
      <stop offset="0" stop-color="#6ea24c"/><stop offset="0.55" stop-color="#7aab57"/><stop offset="1" stop-color="#5f9540"/>
    </linearGradient>
  </defs>
  <path role="img" aria-label="Photo of two children in football jerseys smiling with coloured mouthguards, holding a football" d="M0 0H1200V368Q900 510 600 510Q300 510 0 368Z" fill="url(#heroFill)"/>
  <path d="M50 402Q600 720 1150 402Q600 640 50 402Z" fill="#3dcc2e"/>
</svg>
<div class="abs brand" style="top:183px;left:110px;font-size:70px;color:#fff;line-height:1">TARVEL</div>
<div class="abs brand" style="top:280px;left:112px;font-size:36px;color:#fff">MOUTHGUARDS</div>
<p class="abs" style="top:337px;left:110px;font-size:18px;line-height:1.55;color:#fff">Custom-Made Sports Mouthguards in Perth<br>Protect your smile with a comfortable, professional fit.</p>
<div class="abs btn navy" style="top:409px;left:110px">Book Now<i></i></div>

<h2 class="abs section-title" style="top:776px;left:0;width:1200px">Why Choose Us</h2>
<div class="abs rule" style="top:822px;left:563px"></div>
<p class="abs" style="top:846px;left:0;width:1200px;text-align:center;font-size:18px">Talk to us about our <b>“gap free”</b> mouthguards for eligible private health insurance members.</p>

<div class="feature" style="top:953px;left:105px"><div class="ring"><span><svg width="30" height="30" viewBox="0 0 24 24" fill="none" stroke="#0b2566" stroke-width="1.6"><circle cx="12" cy="9" r="5"/><path d="M4 21c1-5 15-5 16 0"/></svg></span></div>Professionally made by a qualified dental prosthetist</div>
<div class="feature" style="top:953px;left:315px"><div class="ring"><span><svg width="30" height="30" viewBox="0 0 24 24" fill="none" stroke="#0b2566" stroke-width="1.6"><path d="M12 3l7 3v5c0 4-3 7-7 9-4-2-7-5-7-9V6z"/><path d="M9 12l2 2 4-4"/></svg></span></div>Custom fit for comfort, protection, and durability</div>
<div class="feature" style="top:900px;left:514px;color:#0b2566">
  <svg width="152" height="200" viewBox="0 0 152 200" style="display:block;margin:0 auto 6px">
    <circle cx="76" cy="76" r="70" fill="#0b2566"/><circle cx="76" cy="76" r="44" fill="#fff"/><circle cx="76" cy="76" r="34" fill="#3dcc2e"/>
    <path d="M62 70h28v16H62z" fill="none" stroke="#fff" stroke-width="2.5"/><path d="M66 70l10-8 10 8" fill="none" stroke="#fff" stroke-width="2.5"/>
    <path d="M28 140q48 40 96 0" fill="none" stroke="#3dcc2e" stroke-width="6"/>
    <path d="M38 160q38 30 76 0" fill="none" stroke="#3dcc2e" stroke-width="6"/>
    <path d="M50 180q26 18 52 0" fill="none" stroke="#3dcc2e" stroke-width="6"/>
  </svg>Clinic and mobile school/club visits available</div>
<div class="feature" style="top:953px;left:706px"><div class="ring"><span><svg width="30" height="30" viewBox="0 0 24 24" fill="none" stroke="#0b2566" stroke-width="1.6"><rect x="4" y="5" width="16" height="15" rx="2"/><path d="M4 9h16M8 3v4M16 3v4M9 14l2 2 4-4"/></svg></span></div>Available for kids, teens, and adults</div>
<div class="feature" style="top:953px;left:915px"><div class="ring"><span><svg width="30" height="30" viewBox="0 0 24 24" fill="none" stroke="#0b2566" stroke-width="1.6"><rect x="4" y="3" width="6" height="18" rx="1"/><path d="M10 9l6-4 4 6-10 8"/></svg></span></div>Wide range of colours and designs</div>

<svg class="abs" style="top:1263px;left:0" width="1200" height="535" viewBox="0 0 1200 535">
  <rect width="1200" height="535" fill="#0b2566"/>
  <path role="img" aria-label="Photo of a purple and white patterned mouthguard in a purple case" d="M0 0H498Q650 230 470 535H0Z" fill="#8e7fbf"/>
  <path d="M525 50Q650 260 520 480Q600 260 525 50Z" fill="#3dcc2e"/>
</svg>
<div class="abs" style="top:1325px;left:668px;font-family:var(--head);font-size:27px;color:#fff;white-space:nowrap">OUR MOUTHGUARDS</div>
<div class="abs rule" style="top:1377px;left:672px;width:60px"></div>
<ul class="abs points" style="top:1405px;left:672px;width:420px">
  <li><span><b>Maximum Protection -</b> absorbs impact and helps prevent broken teeth, jaw injuries, and concussions.</span></li>
  <li><span><b>Superior Comfort -</b> designed to fit snugly, making it easier to breathe and talk while playing.</span></li>
  <li><span><b>Durability -</b> crafted from high-quality dental materials that outlast off-the-shelf options</span></li>
</ul>
<p class="abs" style="top:1605px;left:672px;width:430px;font-size:15px;line-height:1.55;color:#fff">With over <b>20 years experience</b> in the industry, our dental prosthetist takes care to provide mouthguards that are made with precision and shaped for your comfort and protection.</p>
<div class="abs btn green" style="top:1694px;left:668px">Read More<i></i></div>

<h2 class="abs" style="top:1888px;left:0;width:1200px;text-align:center;font-family:var(--head);font-size:36px;color:var(--navy)">Gallery</h2>
<div class="abs rule" style="top:1938px;left:560px;width:80px"></div>
<div class="tile" role="img" aria-label="Glitter and checkered mouthguards in a clear case" style="top:1965px;left:110px;width:313px;height:185px;background:linear-gradient(135deg,#b9a9cf,#4aa8b0)"></div>
<div class="tile" role="img" aria-label="Maroon mouthguard in a white case" style="top:2163px;left:110px;width:149px;height:152px;background:linear-gradient(135deg,#d8d2cc,#8c3a4a)"></div>
<div class="tile" role="img" aria-label="Red and pink mouthguards in cases" style="top:2163px;left:277px;width:149px;height:152px;background:linear-gradient(135deg,#c82020,#e4b8c4)"></div>
<div class="tile" role="img" aria-label="Two round blue glitter mouthguard blanks on wood" style="top:1965px;left:443px;width:314px;height:350px;background:linear-gradient(180deg,#2a7fa8,#1f5f8c)"></div>
<div class="tile" role="img" aria-label="Pink marbled mouthguard in a purple case" style="top:1963px;left:775px;width:313px;height:167px;background:linear-gradient(135deg,#7e5aa8,#ee85b5)"></div>
<div class="tile" role="img" aria-label="Glitter mouthguard in a teal case" style="top:2146px;left:775px;width:313px;height:168px;background:linear-gradient(135deg,#2bb5b5,#8f8aa0)"></div>
<div class="abs btn navy" style="top:2348px;left:520px">View All<i></i></div>

<svg class="abs" style="top:2480px;left:0" width="1200" height="445" viewBox="0 0 1200 445">
  <path d="M0 200Q600 -40 1200 200V445H0Z" fill="#0b2566"/>
  <path d="M50 180Q600 -110 1150 180Q600 -60 50 180Z" fill="#3dcc2e"/>
</svg>
<div class="abs" style="top:2628px;left:0;width:1200px;text-align:center;font-family:var(--head);font-size:26px;color:#fff">OUR SERVICE PROVIDER</div>
<div class="abs rule" style="top:2678px;left:586px;width:60px"></div>
<div class="abs" style="top:2735px;left:188px;width:398px;height:80px;background:#fff;border-radius:4px;display:flex;align-items:center;justify-content:center;gap:18px;font-family:var(--head);font-size:34px;color:var(--navy)"><span style="width:26px;height:26px;border-radius:50%;background:var(--navy)"></span>MORVEX</div>
<div class="abs" style="top:2735px;left:610px;width:398px;height:80px;background:#fff;border-radius:4px;display:flex;align-items:center;justify-content:center;font-family:var(--head);font-size:17px;color:var(--navy)">WESTSHORE DENTURE STUDIO</div>

<div class="abs brand" style="top:3010px;left:0;width:1200px;text-align:center;font-size:58px;line-height:1">TARVEL</div>
<div class="abs brand" style="top:3090px;left:0;width:1200px;text-align:center;font-size:30px">MOUTHGUARDS</div>
<nav class="abs footnav" style="top:3160px;left:0;width:1200px">
  <span>Home</span><span>About Us</span><span>Why Choose a Custom Mouthguard?</span><span>Gallery</span><span>FAQ</span><span>Contact Us</span>
</nav>
<div class="fcontact" style="top:3213px;left:108px"><div class="ring"><span><svg width="14" height="14" viewBox="0 0 24 24"><path fill="#fff" d="M6.6 10.8a15 15 0 0 0 6.6 6.6l2.2-2.2c.3-.3.7-.4 1-.2 1.1.4 2.3.6 3.6.6.6 0 1 .4 1 1V20c0 .6-.4 1-1 1A17 17 0 0 1 3 4c0-.6.4-1 1-1h3.5c.6 0 1 .4 1 1 0 1.3.2 2.5.6 3.6.1.3 0 .7-.2 1z"/></svg></span></div><div>PHONE:<br>08 6100 2755</div></div>
<div class="divider" style="top:3213px;left:328px"></div>
<div class="fcontact" style="top:3213px;left:372px"><div class="ring"><span><svg width="14" height="14" viewBox="0 0 24 24"><path fill="#fff" d="M3 5h18v14H3zm2 2v.5l7 4.5 7-4.5V7z"/></svg></span></div><div>EMAIL:<br>info@westshoredenture.com.au</div></div>
<div class="divider" style="top:3213px;left:752px"></div>
<div class="fcontact" style="top:3213px;left:786px"><div class="ring"><span><svg width="14" height="14" viewBox="0 0 24 24"><path fill="#fff" d="M12 2a7 7 0 0 0-7 7c0 5 7 13 7 13s7-8 7-13a7 7 0 0 0-7-7zm0 9.5A2.5 2.5 0 1 1 12 6.5a2.5 2.5 0 0 1 0 5z"/></svg></span></div><div>ADDRESS:<br>Unit 4/12 Harbour Cres,<br>Kelvale WA 6071</div></div>
<p class="abs" style="top:3320px;left:0;width:1200px;text-align:center;font-size:14px">COPYRIGHTS@2025.COMPANY NAME.ALL RIGHTS RESERVED</p>

</div>
</body>
</html>
```